Bottom fuel dispenser panel

Design the fuel dispenser lower panel graphics based on our brand “tandrel”
I will attach the brand logo and picture of the dispenser along with some other examples of other brands portraying their logos.

Target Market(s)

Petrol pump consumers

Industry/Entity Type

Oil and gas retailer

Requirements
Must have
• Theme that matches our brand
Nice to have
• Please refer to the image of the gas station in tandrel branded photos. Size of the bottom panel is 28” by 45”.
Should not have
• Too many colors

```html
<!DOCTYPE html>
<html lang="en">
<head>
<meta charset="utf-8">
<title>tandrel – Dispenser Lower Panel</title>
<link rel="stylesheet" href="https://fonts.googleapis.com/css2?family=Open+Sans:wght@800&display=swap">
<style>
  :root {
    --page-bg: #ffffff;
    --panel-bg: #ffffff;
    --brand-green: #99cb38;
    --brand-green-soft: #cfe6a0;
    --brand-black: #000000;
  }
  html, body {
    margin: 0;
    padding: 0;
    width: 1200px;
    height: 1200px;
    overflow: hidden;
    background: var(--page-bg);
  }
  .canvas {
    position: relative;
    width: 1200px;
    height: 1200px;
  }
  .dispenser-panel {
    position: absolute;
    left: 100px;
    top: 289px;
    width: 1000px;
    height: 622px;
    background: var(--panel-bg);
    overflow: hidden;
  }
  .panel-graphic {
    position: absolute;
    inset: 0;
    background: linear-gradient(152deg,
      var(--panel-bg) 0%,
      var(--panel-bg) 48%,
      var(--brand-green-soft) 68%,
      var(--brand-green) 100%);
  }
  .brand-lockup {
    position: absolute;
    left: 0;
    top: 0;
    width: 1000px;
    height: 622px;
  }
  .brand-name {
    font-family: "Open Sans", sans-serif;
    font-weight: 800;
    font-size: 159px;
    letter-spacing: -6px;
    fill: var(--brand-black);
  }
</style>
</head>
<body>
  <main class="canvas">
    <section class="dispenser-panel">
      <div class="panel-graphic" role="img" aria-label="Sweeping black and green brand band rising across the lower panel"></div>
      <svg class="brand-lockup" viewBox="0 0 1000 622" xmlns="http://www.w3.org/2000/svg" aria-label="tandrel">
        <text class="brand-name" x="60" y="261">tandrel</text>
      </svg>
    </section>
  </main>
</body>
</html>
```